Pre-workout label and Super Greens label for Vantora Nutrition Supplements

I need a label design for Club Vantora's 2 supplements. The first is a Pre-workout. The Pre-workout label needs to be 11.25 x 2.5 inches. This label will go on a black container. The second is a Super-Green. The Super-Green label should be 11.25 x 4.25 inches and will go on a white container. We have been selling these for a few years but the current labels are a little meh. I'd like something trendier and bolder. Must keep the Club Vantora branding. All the nurtition data must appear . I attached the current designs so you can know the flavors, nutrtional data etc. Thank you!
Updates

I can upload the Club Vantora logo! If anyone can tell me how to do that.

```html
<!DOCTYPE html>
<html lang="en">
<head>
<meta charset="utf-8">
<title>Vantora Nutrition – Label Set</title>
<link href="https://fonts.googleapis.com/css2?family=Arimo:wght@400;700&family=Barlow+Condensed:wght@600&family=Russo+One&display=swap" rel="stylesheet">
<style>
:root{
  --ink:#111;
  --white:#fff;
  --page:#fff;
  --brand-red:#d7192f;
  --green-deep:#2f8a22;
  --green:#6fb83a;
  --green-soft:#cfe6b4;
  --red-deep:#9c0d18;
  --red:#d81f32;
  --red-soft:#f6c6cc;
  --grey:#9a9a9a;
  --muted:#777;
  --rule:#cfcfcf;
}
*{box-sizing:border-box;margin:0;padding:0}
html,body{width:1200px;height:2400px;overflow:hidden;background:var(--page)}
body{position:relative;font-family:"Arimo",Arial,sans-serif;color:var(--ink)}
ul{list-style:none}

.brand{position:absolute;display:flex;align-items:center;gap:10px;font-family:"Barlow Condensed",sans-serif;font-weight:600;letter-spacing:.08em;text-transform:uppercase;color:var(--ink)}
.brand-mark{background:var(--brand-red);display:block}
.page-header{top:90px;left:0;width:1200px;justify-content:center;font-size:44px}
.page-header .brand-mark{width:40px;height:40px}

.divider{position:absolute;left:370px;width:460px;top:1280px;height:1px;background:var(--rule)}

.label{position:absolute;left:70px;width:1060px;overflow:hidden}
.label-green{top:520px;height:400px}
.label-red{top:1660px;height:236px}

.label-art{position:absolute;inset:0}
.label-green .label-art{background:
  radial-gradient(ellipse 230px 190px at 50% 48%,rgba(255,255,255,.97) 60%,rgba(255,255,255,0) 100%),
  linear-gradient(90deg,var(--green-deep) 0%,var(--green) 18%,var(--green-soft) 32%,#fff 40%,#fff 60%,var(--green-soft) 70%,var(--green) 84%,var(--green-deep) 100%)}
.label-red .label-art{background:
  radial-gradient(ellipse 220px 110px at 50% 40%,rgba(255,255,255,.92) 55%,rgba(255,255,255,0) 100%),
  linear-gradient(90deg,var(--red-deep) 0%,var(--red) 20%,var(--red-soft) 40%,#fff 50%,var(--red-soft) 60%,var(--red) 80%,var(--red-deep) 100%)}

.info-box{position:absolute;background:var(--white);border:1px solid #888;border-radius:8px;padding:8px 12px;line-height:1.25}
.info-box b{font-weight:700}
.label-green .info-box{font-size:8.6px}
.label-green .directions{left:66px;top:34px;width:146px;height:70px}
.label-green .caution{left:66px;top:124px;width:146px;height:130px}
.label-green .disclaimer{left:66px;top:320px;width:146px;height:30px;font-size:4.6px;font-weight:700;text-align:center;padding:5px 6px}

.label-red .info-box{font-size:4.2px;border-radius:6px;padding:6px 8px}
.label-red .directions{left:30px;top:14px;width:150px;height:94px}
.label-red .disclaimer{left:30px;top:118px;width:88px;height:20px;font-size:3.2px;padding:3px 5px}

.label .brand{justify-content:center;flex-direction:column;gap:6px;left:0;width:1060px}
.label-green .brand{top:18px;font-size:17px}
.label-green .brand-mark{width:22px;height:22px}
.label-red .brand{top:10px;font-size:9px;gap:4px}
.label-red .brand-mark{width:13px;height:13px}

.product-name{position:absolute;left:0;width:1060px;text-align:center;font-family:"Russo One",sans-serif;text-transform:uppercase;letter-spacing:.01em;transform:skewX(-12deg);color:var(--ink);white-space:nowrap}
.label-green .product-name{top:108px;font-size:46px}
.label-red .product-name{top:44px;font-size:35px}
.product-name .dim{color:var(--grey)}

.flavor{position:absolute;left:50%;transform:translateX(-50%);font-family:"Barlow Condensed",sans-serif;font-weight:600;font-style:italic;letter-spacing:.05em;text-transform:uppercase;white-space:nowrap;clip-path:polygon(6% 0,100% 0,94% 100%,0 100%)}
.label-green .flavor{top:186px;background:var(--green);color:#101a08;font-size:15px;padding:3px 22px}
.label-red .flavor{top:90px;background:var(--red);color:var(--white);font-size:10px;padding:2px 14px}

.benefits{position:absolute;left:0;width:1060px;display:flex;justify-content:center;text-align:center;text-transform:uppercase}
.benefit{display:flex;flex-direction:column;align-items:center}
.label-green .benefits{top:232px;gap:36px}
.label-green .benefit{width:110px;font-size:9.5px;line-height:1.1}
.label-green .benefit svg{width:40px;height:40px;margin-bottom:14px;color:var(--green)}
.label-red .benefits{top:122px;gap:26px}
.label-red .benefit{width:80px;font-size:6.4px;font-weight:700;line-height:1.15}
.label-red .benefit svg{width:14px;height:14px;margin-bottom:6px}
.label-red .benefit small{font-weight:400;font-size:5.4px;color:var(--muted)}

.net{position:absolute;font-weight:700;white-space:nowrap}
.label-green .net{top:358px;font-size:9.5px}
.label-green .net-left{left:378px}
.label-green .net-right{left:590px}
.label-red .net{top:206px;font-size:5.4px;text-transform:uppercase;color:var(--ink)}
.label-red .net-left{left:380px}
.label-red .net-right{left:590px}

.facts{position:absolute;background:var(--white);border:1px solid #333;padding:4px 5px;line-height:1.2}
.facts h3{font-size:10px;font-weight:700;border-bottom:2px solid #333;margin-bottom:2px}
.facts table{width:100%;border-collapse:collapse}
.facts td{padding:.6px 0;border-bottom:.5px solid #bbb;vertical-align:top}
.facts td+td{text-align:right;white-space:nowrap;padding-left:4px}
.facts .blend td:first-child b{display:block}
.label-green .facts{left:830px;top:48px;width:196px;height:282px;font-size:4.3px}
.label-red .facts{left:720px;top:14px;width:170px;height:104px;font-size:3.6px}
.label-red .facts h3{font-size:6px}
.fine{position:absolute;font-size:4.2px;line-height:1.3}
.label-green .fine{left:830px;top:334px;width:196px}
.label-red .fine{left:720px;top:122px;width:170px;color:var(--white);font-size:3.6px}
</style>
</head>
<body>

<header class="brand page-header"><span class="brand-mark"></span>Vantora Nutrition</header>

<section class="label label-green" aria-label="Ultra Verde label, flat">
  <div class="label-art" role="img" aria-label="Faceted green low-poly background fading to white in the centre"></div>

  <div class="info-box directions"><b>Directions:</b> Mix one (1) scoop into 6-8oz of your favorite non-citrus juice, water, smoothie, or protein shake.</div>
  <div class="info-box caution"><b>CAUTION:</b> As with any dietary supplement, consult your healthcare practitioner before using this product, especially if you are pregnant, nursing, anticipate surgery, take medication on a regular basis or are otherwise under medical supervision. Store in a cool, dry place. Keep out of reach of children.</div>
  <div class="info-box disclaimer">*These statements have not been evaluated by the Food and Drug Administration. This product is not intended to diagnose, treat, cure or prevent any disease.</div>

  <div class="brand"><span class="brand-mark"></span>Vantora Nutrition</div>
  <h1 class="product-name">Ultra Verde</h1>
  <div class="flavor">Pear Nutmeg</div>

  <ul class="benefits">
    <li class="benefit">
      <svg viewBox="0 0 40 40" fill="none" stroke="currentColor" stroke-width="5"><path d="M20 20c-4-6-8-8-11-8a8 8 0 0 0 0 16c3 0 7-2 11-8s8-8 11-8a8 8 0 0 1 0 16c-3 0-7-2-11-8z"/></svg>
      Detox<br>Body *
    </li>
    <li class="benefit">
      <svg viewBox="0 0 40 40" fill="none" stroke="currentColor" stroke-width="3.5" stroke-linecap="round"><path d="M20 2v6M20 8h6a4 4 0 0 1 0 8H14a4 4 0 0 0 0 8h12a4 4 0 0 1 0 8H14a4 4 0 0 0 0 8"/></svg>
      Promote Healthy<br>Digestion *
    </li>
    <li class="benefit">
      <svg viewBox="0 0 40 40"><path d="M20 2l15 6v12c0 9-7 15-15 18C12 35 5 29 5 20V8z" fill="currentColor"/><path d="M20 12v16M12 20h16" stroke="#fff" stroke-width="4"/></svg>
      Support<br>Immunity *
    </li>
  </ul>

  <span class="net net-left">Dietary Supplement</span>
  <span class="net net-right">30 Servings&nbsp; 270g (9.5oz)</span>

  <div class="facts">
    <h3>Supplement Facts</h3>
    <p>Serving Size: Approx. 1 Scoop (9 g)<br>Servings per Container: 30</p>
    <table>
      <tr><td></td><td>Amount per Serving &nbsp; %DV</td></tr>
      <tr><td>Calories</td><td>40</td></tr>
      <tr><td>Total Carbohydrates</td><td>1.5 g &nbsp; 2%</td></tr>
      <tr><td>&nbsp; Dietary Fiber</td><td>0 g &nbsp; 2%</td></tr>
      <tr><td>&nbsp; Total Sugars</td><td>&lt;1 g &nbsp; †</td></tr>
      <tr><td>Vitamin E (as DI-Alpha Tocopheryl Acetate)</td><td>46 mg &nbsp; 307%</td></tr>
      <tr><td>Potassium</td><td>110 mg &nbsp; 2%</td></tr>
      <tr class="blend"><td><b>Green Health Blend</b>Soy Lecithin Powder, Pear Fruit Powder, Barley Grass Powder, Alfalfa Herb Powder, Wheat Grass Powder, Spinach Leaf Powder</td><td>5.6 g &nbsp; †</td></tr>
      <tr class="blend"><td><b>Energy Blend</b>Spirulina Whole Plant Powder, Beet Root Powder, Green Tea Leaf Extract</td><td>1.41 g &nbsp; †</td></tr>
      <tr class="blend"><td><b>Detox Blend</b>Acerola Berry Powder, Parsley Leaf Powder, Licorice Root Powder, Milk Thistle Seed Extract</td><td>420 mg &nbsp; †</td></tr>
      <tr class="blend"><td><b>Alkalinity Blend</b>Chlorella Cracked Cell Wall Powder, Ginkgo Leaf Extract, Grape Seed Extract</td><td>340 mg &nbsp; †</td></tr>
      <tr class="blend"><td><b>Probiotic Blend Complex</b>Lactobacillus acidophilus, Bifidobacterium bifidum, Streptococcus thermophilus</td><td>150 mg &nbsp; †</td></tr>
      <tr class="blend"><td><b>Enzyme Blend</b>Maltodextrin, Inulin, Bromelain, Papain, Cellulase, Lipase, Protease</td><td>125 mg &nbsp; †</td></tr>
    </table>
    <p>Percent Daily Values are based on a 2,000 calorie diet.<br>† Daily Value (DV) not established.</p>
  </div>
  <p class="fine"><b>Other Ingredients:</b> Organic Nutmeg Powder, Natural Flavors, Citric Acid, Stevia Leaf Extract, Sucralose.<br>Contains: Tree Nuts, Wheat, and Soy.<br><b>Formulated by:</b> Club Vantora, 220 Ridge Way, Cedar Falls, WY 82000 (555) 010-2040</p>
</section>

<div class="divider"></div>

<section class="label label-red" aria-label="Pre-Workout label, flat">
  <div class="label-art" role="img" aria-label="Faceted red low-poly background fading to white in the centre"></div>

  <div class="info-box directions"><b>Directions:</b> Use on training days only. Mix 1 scoop with 8-10 oz of cold water 15-30 minutes prior to training.<br><br><b>Warning:</b> Not intended for use by persons under age 18. Do not exceed recommended dose. Do not combine with other sources of caffeine, including coffee, tea, soda, or other stimulants. Consult your physician prior to use if you are pregnant or nursing, or if you are taking medication or have a medical condition, including heart, liver, kidney or thyroid disease, high blood pressure, anxiety, or glaucoma. Discontinue use 2 weeks prior to surgery or if you experience rapid heartbeat, dizziness, severe headaches, or shortness of breath. Keep out of reach of children.</div>
  <div class="info-box disclaimer">*These statements have not been evaluated by the Food and Drug Administration. This product is not intended to diagnose, treat, cure or prevent any disease.</div>

  <div class="brand"><span class="brand-mark"></span>Vantora Nutrition</div>
  <h1 class="product-name"><span class="dim">Pre</span>-Workout</h1>
  <div class="flavor">Melon Splash</div>

  <ul class="benefits">
    <li class="benefit">
      <svg viewBox="0 0 14 14"><rect width="14" height="14" rx="2" fill="#111"/><path d="M8 2L4 8h3l-1 4 4-6H7z" fill="#fff"/></svg>
      Energy†<small>Caffeine</small>
    </li>
    <li class="benefit">
      <svg viewBox="0 0 14 14"><rect width="14" height="14" rx="2" fill="#111"/><path d="M7 2l4 5H8.5v5h-3V7H3z" fill="#fff"/></svg>
      Performance†<small>Beta-Alanine</small>
    </li>
    <li class="benefit">
      <svg viewBox="0 0 14 14"><rect width="14" height="14" rx="2" fill="#111"/><path d="M3 5v4M11 5v4M4.5 4v6M9.5 4v6M4.5 7h5" stroke="#fff" stroke-width="1.2"/></svg>
      Strength†<small>Creatine</small>
    </li>
  </ul>

  <span class="net net-left">Dietary Supplement</span>
  <span class="net net-right">30 Servings 240g (8.5oz)</span>

  <div class="facts">
    <h3>Supplement Facts</h3>
    <table>
      <tr><td></td><td>Amount per Serving &nbsp; %DV</td></tr>
      <tr><td>Calories</td><td>5 &nbsp;</td></tr>
      <tr><td>Vitamin B6 (as Pyridoxal-5'-Phosphate)</td><td>1.02 mg &nbsp; 60%</td></tr>
      <tr><td>Folate</td><td>250 mcg DFE &nbsp; 63%</td></tr>
      <tr><td>Vitamin B12 (as Methylcobalamin)</td><td>20 mcg &nbsp; 833%</td></tr>
      <tr><td>Beta-Alanine</td><td>1.6 g &nbsp; †</td></tr>
      <tr><td>Creatine Monohydrate</td><td>1.5 g &nbsp; †</td></tr>
      <tr><td>L-Arginine Alpha-Ketoglutarate</td><td>1 g &nbsp; †</td></tr>
      <tr><td>Betaine Anhydrous</td><td>500 mg &nbsp; †</td></tr>
      <tr><td>Caffeine Anhydrous</td><td>200 mg &nbsp; †</td></tr>
      <tr><td>Huperzine A</td><td>40 mcg &nbsp; †</td></tr>
    </table>
    <p>† Daily Value (DV) not established.</p>
  </div>
  <p class="fine"><b>Other Ingredients:</b> Citric Acid, Melon Fruit Powder, Silicon Dioxide, Natural and Artificial Flavors, Sucralose, FD&amp;C Red #40.<br><br><b>Formulated by:</b> Club Vantora, 220 Ridge Way, Cedar Falls, WY 82000 (555) 010-2040</p>
</section>

</body>
</html>
```